Virtual Restaurant Menu Design

I need a menu displayed on monitors of my casual restaurant. I currently have 3 monitors, I could potentially add 2 more. My menu is quite large but I need the monitors to each display part of the menu in a manner that is visually appealing but still easy to read. That means there needs to be 3 separate files where one file will be displayed on one monitor and the other two files on the the other monitors. Looking for a classic and clean look. I have attached menu for reference. Including some professional pictures incase you can incorporate them into the design for that section. Catering and beverage section of menu need not be displayed. I would like an editable version of this incase my prices change in the future.Good performance on this will very likely lead to future work as I have specials that I like to change and display on a monthly basis.
Italian Restaurant

```html
<!DOCTYPE html>
<html lang="en">
<head>
<meta charset="utf-8">
<title>Pasta, Subs &amp; Desserts Menu Board</title>
<link href="https://fonts.googleapis.com/css2?family=Alfa+Slab+One&family=Oswald:wght@400;500;600;700&family=Lora:wght@400&display=swap" rel="stylesheet">
<style>
:root{
  --bg:#f1e1d9;
  --red:#c3474b;
  --ink:#2b2323;
  --line:#3a2e2e;
  --black:#111;
  --photo-pasta:#c99a5c;
  --photo-plate:#d8d4cc;
  --photo-dessert:#b9b7b3;
  --photo-sub:#c98f4e;
}
*{margin:0;padding:0;box-sizing:border-box}
html,body{width:1200px;height:675px;overflow:hidden;background:var(--bg)}
.board{position:relative;width:1200px;height:675px;background:var(--bg);color:var(--ink);font-family:'Oswald',sans-serif}
.photo{position:absolute;border-radius:14px}
.photo--penne{left:34px;top:48px;width:530px;height:122px;background:radial-gradient(ellipse at 55% 50%,var(--photo-pasta) 0 45%,var(--photo-plate) 60%,#7d7a76 100%)}
.photo--piccata{left:34px;top:510px;width:530px;height:122px;background:radial-gradient(ellipse at 50% 50%,#e6d8a8 0 40%,var(--photo-plate) 65%,#8a8783 100%)}
.photo--cannoli{left:601px;top:312px;width:277px;height:206px;border-radius:6px;background:radial-gradient(circle at 50% 50%,#6b5446 0 18%,var(--photo-dessert) 45%,#8c8a88 100%)}
.photo--sub{left:896px;top:262px;width:276px;height:168px;border-radius:45%;background:radial-gradient(ellipse at 50% 55%,var(--photo-sub) 0 40%,rgba(201,143,78,.4) 60%,rgba(241,225,217,0) 72%)}
.tag{position:absolute;left:50px;top:30px;width:127px;height:54px;background:var(--black);color:#fff;font:600 30px/54px 'Oswald',sans-serif;text-align:center;transform:rotate(-2deg);letter-spacing:1px}
.title{position:absolute;left:200px;top:180px;width:192px;text-align:center;font:38px/1 'Alfa Slab One',serif;color:var(--red);text-shadow:3px 3px 0 #5b3a3a}
.panel{position:absolute;border:1.5px solid var(--line);border-radius:5px}
.panel__head{position:absolute;left:4px;top:-15px;background:var(--bg);padding:0 5px;font:500 21px/1 'Oswald',sans-serif;color:var(--red);letter-spacing:.5px}
.note{text-align:center;font:500 9.5px/1.3 'Oswald',sans-serif;text-transform:uppercase;letter-spacing:.4px}
.price-line{text-align:center;font:500 9.5px/1.3 'Oswald',sans-serif;text-transform:uppercase}
.price-line em{font-style:normal;color:var(--red)}
.item{margin-top:3px}
.item__name{font:600 17px/1 'Oswald',sans-serif;text-transform:uppercase;display:flex;justify-content:space-between;align-items:baseline}
.item__price{font:500 9.5px/1 'Oswald',sans-serif;color:var(--red)}
.item__desc{font:400 8.4px/1.15 'Lora',serif;margin-top:1px}
.panel--chicken{left:19px;top:248px;width:278px;height:227px;padding:13px 12px 0}
.panel--seafood{left:308px;top:248px;width:278px;height:227px;padding:21px 12px 0}
.panel--deli{left:601px;top:40px;width:277px;height:258px;padding:14px 12px 0}
.panel--gourmet{left:892px;top:42px;width:278px;height:209px;padding:13px 12px 0}
.panel--desserts{left:601px;top:546px;width:277px;height:103px;padding:14px 12px 0}
.panel--bev{left:892px;top:458px;width:278px;height:191px;padding:16px 12px 0}
.panel--deli .item,.panel--gourmet .item{margin-top:2px}
.panel--deli .first,.panel--gourmet .first{margin-top:6px}
.desserts{display:grid;grid-template-columns:1fr 1fr;column-gap:12px}
.dessert{display:flex;justify-content:space-between;align-items:flex-end;font:600 16px/0.98 'Oswald',sans-serif;text-transform:uppercase;margin-bottom:4px}
.dessert span{font:500 9.5px/1.4 'Oswald',sans-serif;color:var(--red)}
.gelato-sizes{text-align:right;font:500 9.5px/1 'Oswald',sans-serif}
.gelato-sizes em{font-style:normal;color:var(--red)}
.house{margin-top:10px;text-align:center;font:500 10px/1.1 'Oswald',sans-serif;text-transform:uppercase}
</style>
</head>
<body>
<main class="board">
  <div class="photo photo--penne" role="img" aria-label="Plate of creamy penne with sun-dried tomatoes and chicken"></div>
  <div class="tag">PASTA</div>
  <h1 class="title">PASTA</h1>

  <section class="panel panel--chicken">
    <h2 class="panel__head">CHICKEN AND VEAL</h2>
    <p class="note">Includes a side salad and garlic bread</p>
    <p class="price-line"><em>Chicken entrees</em> 17.50 · <em>Veal entrees</em> 19.95</p>
    <div class="item" style="margin-top:9px"><div class="item__name">Piccata</div><p class="item__desc">With capers sautéed in a white garlic lemon sauce.</p></div>
    <div class="item"><div class="item__name">Marsala</div><p class="item__desc">With mushrooms in Marsala wine sauce.</p></div>
    <div class="item"><div class="item__name">Parmigiana</div><p class="item__desc">Topped with mozzarella &amp; tomato sauce.</p></div>
    <div class="item"><div class="item__name">Al Pesto</div><p class="item__desc">Sautéed with mushrooms in creamy pesto sauce,<br>served over penne.</p></div>
    <div class="item"><div class="item__name">Brunello</div><p class="item__desc">Mushrooms &amp; sun-dried tomatoes in<br>a creamy pink sauce</p></div>
  </section>

  <section class="panel panel--seafood">
    <h2 class="panel__head">SEAFOOD</h2>
    <p class="note">Includes a side salad and garlic bread</p>
    <div class="item" style="margin-top:16px"><div class="item__name">Fettuccine Mediterraneo <span class="item__price">19.95</span></div><p class="item__desc">Combination of fresh jumbo shrimp, scallops &amp;<br>crabmeat in a light cream sauce</p></div>
    <div class="item"><div class="item__name">Linguini alla Posillipo <span class="item__price">19.95</span></div><p class="item__desc">Clams, mussels, squid &amp; shrimp in light marinara.</p></div>
    <div class="item"><div class="item__name">Shrimp Scampi <span class="item__price">18.95</span></div><p class="item__desc">Topped with mozzarella &amp; tomato sauce.</p></div>
    <div class="item"><div class="item__name">Shrimp alla Fra Diavolo <span class="item__price">18.95</span></div><p class="item__desc">Fresh shrimp served with a spicy marinara sauce.</p></div>
  </section>

  <div class="photo photo--piccata" role="img" aria-label="Chicken piccata with capers and lemon over spaghetti"></div>

  <section class="panel panel--deli">
    <h2 class="panel__head">DELI SUBS</h2>
    <p class="price-line"><em>Whole sub</em> 8.50 · <em>Half sub</em> 5.50</p>
    <p class="note" style="font-size:7.5px">Served with lettuce, tomatoes, onions, hot peppers and<br>mayo unless otherwise specified.</p>
    <p class="price-line" style="font-size:8px;margin-top:2px"><em>Extra meat</em> 2.50 · <em>Extra cheese</em> 1.50 · <em>Extra toppings</em> .50 each</p>
    <div class="item first"><div class="item__name">Steak and Cheese</div><p class="item__desc">High quality Philly style steak grilled with onions.<br>A customer favorite!</p></div>
    <div class="item"><div class="item__name">Chicken Steak</div></div>
    <div class="item"><div class="item__name">Prosciutto Mozzarella</div><p class="item__desc">(Hot or Cold) Served with Italian dressing.</p></div>
    <div class="item"><div class="item__name">Ham and Cheese</div><p class="item__desc">(Hot or Cold) Served with Italian dressing.</p></div>
    <div class="item"><div class="item__name">Turkey and Cheese</div><p class="item__desc">(Hot or Cold) Served with Italian dressing.</p></div>
    <div class="item"><div class="item__name">Italian Hoagie</div><p class="item__desc">(Hot or Cold) Salami, ham, cheese &amp; Italian dressing.</p></div>
  </section>

  <div class="photo photo--cannoli" role="img" aria-label="Chocolate-dipped cannoli with cream filling dusted with sugar"></div>

  <section class="panel panel--desserts">
    <h2 class="panel__head">DESSERTS</h2>
    <div class="desserts">
      <div>
        <div class="dessert">Italian<br>Cannoli <span>2.95</span></div>
        <div class="dessert">Tiramisu <span>4.95</span></div>
        <div class="dessert">Cheesecake <span>4.95</span></div>
      </div>
      <div>
        <div class="dessert">Sfogliatella <span>2.95</span></div>
        <div class="dessert">Chocolate<br>Mousse Cup <span>4.95</span></div>
        <div class="dessert" style="margin-bottom:1px">Gelato Italiano</div>
        <p class="gelato-sizes">SMALL <em>3.95</em> REG <em>4.95</em></p>
      </div>
    </div>
  </section>

  <section class="panel panel--gourmet">
    <h2 class="panel__head">GOURMET SUBS</h2>
    <p class="price-line"><em>Whole sub</em> 8.95 · <em>Half sub</em> 5.95</p>
    <p class="price-line" style="font-size:8px"><em>Extra meat</em> 2.50 · <em>Extra cheese</em> 1.50 · <em>Extra toppings</em> .50 each</p>
    <div class="item first" style="margin-top:3px"><div class="item__name">Parmigiana</div><p class="item__desc">CHOOSE FROM: Meatball, Chicken or Eggplant with<br>tomato sauce &amp; mozzarella</p></div>
    <div class="item"><div class="item__name">Caprese</div><p class="item__desc">(Hot or Cold) Fresh tomatoes &amp; mozzarella drizzled with<br>olive oil, topped with basil</p></div>
    <div class="item"><div class="item__name">Veal Parmigiana</div><p class="item__desc">Tomato sauce &amp; mozzarella</p></div>
    <div class="item"><div class="item__name">Grilled Italian Sausage</div><p class="item__desc">Peppers, onions &amp; cheese</p></div>
    <div class="item"><div class="item__name">Veggie Subs</div><p class="item__desc">Seasonal vegetables, please inquire.</p></div>
  </section>

  <div class="photo photo--sub" role="img" aria-label="Chicken sub with tomatoes, peppers and basil"></div>

  <section class="panel panel--bev">
    <h2 class="panel__head">BEVERAGES</h2>
    <div class="item" style="margin-top:2px"><div class="item__name">Soft Drinks</div><p class="item__desc">Classic Cola, Diet Cola, Cherry Cola, Root Beer, Lime Soda,<br>Lemonade or Iced Tea</p><p class="price-line"><em>2 liter</em> 3.75 · <em>20 oz bottle</em> 2.00</p></div>
    <div class="item" style="margin-top:5px"><div class="item__name">Sorgente Chiara Drinks <span class="item__price">2.50</span></div><p class="item__desc">Sparkling Water, Still Spring Water, Aranciata, Limonata,<br>Peach Iced Tea or Lemon Iced Tea</p></div>
    <div class="item" style="margin-top:6px"><div class="item__name" style="line-height:1">Cappuccino, Hot Tea,<br>Espresso and Coffee <span class="item__price">3.00</span></div></div>
    <p class="house">We serve beer and wine in house,<br>please ask for our selection.</p>
  </section>
</main>
</body>
</html>
```